Small Accounting Practice needs something creative

We need a business card design for a new small accounting practice based in Perth, Australia. The name of the practice is 'Kelvarin Ledger Group Pty Ltd'. We providing Tax, Bookkeeping and Accounting services. Our target are individuals and small businesses. We want the design to be simply and creative. Also, we can the design can help us to gain people's trust.

Target Market(s)

Individuals and small businesses.

Industry/Entity Type

Accounting

Colors

Designer to choose colors to be used in the design.

```html
<!DOCTYPE html>
<html lang="en">
<head>
<meta charset="utf-8">
<title>Kelvarin Ledger Group – Business Card</title>
<link rel="stylesheet" href="https://fonts.googleapis.com/css2?family=Arvo:wght@400;700&family=Raleway:wght@300&family=Tinos:wght@400;700&family=Roboto+Condensed:wght@400;700&display=swap">
<style>
  :root {
    --page: #ffffff;
    --card-grey: #e2e1df;
    --band-blue: #8799c4;
    --band-navy: #55627e;
    --back-blue: #8c9cc6;
    --ink: #111111;
    --paper-white: #f4f5f8;
    --guide: rgba(255,255,255,0.85);
  }
  * { margin: 0; padding: 0; box-sizing: border-box; }
  html, body { width: 1200px; height: 1000px; overflow: hidden; background: var(--page); }
  .canvas { position: relative; width: 1200px; height: 1000px; }

  .card { position: absolute; left: 250px; width: 755px; height: 410px; overflow: hidden; }

  /* Front */
  .card-front { top: 70px; background: var(--card-grey); }
  .band-main { position: absolute; left: 0; right: 0; top: 45px; height: 305px; background: var(--band-blue); }
  .band-name { position: absolute; left: 0; right: 0; top: 155px; height: 56px; background: var(--band-navy); }
  .trim-line { position: absolute; top: 0; bottom: 0; width: 1px; background: var(--guide); }
  .trim-line.left { left: 72px; }
  .trim-line.right { left: 686px; }

  .headline { position: absolute; left: 82px; top: 62px; display: flex; align-items: flex-end; }
  .role-main { font-family: "Arvo", serif; font-size: 56px; color: var(--paper-white); line-height: 1; letter-spacing: -1px; }
  .ampersand { font-family: "Arvo", serif; font-weight: 700; font-size: 44px; color: var(--ink); margin: 0 8px 0 6px; line-height: 1; }
  .role-sub { font-family: "Tinos", serif; color: var(--ink); font-size: 22px; line-height: 1.15; text-align: center; font-variant: small-caps; letter-spacing: 0.5px; margin-bottom: 4px; }

  .person-name { position: absolute; left: 262px; top: 152px; font-family: "Raleway", sans-serif; font-weight: 300; font-size: 50px; letter-spacing: 1px; line-height: 1; }
  .person-name .first { color: var(--paper-white); }
  .person-name .last { color: var(--ink); }

  .credential { position: absolute; left: 192px; top: 214px; font-family: "Raleway", sans-serif; font-weight: 300; font-size: 25px; letter-spacing: 1px; }
  .credential .light { color: var(--paper-white); }
  .credential .dark { color: var(--ink); }

  .contact-email { position: absolute; left: 92px; top: 292px; }
  .contact-phone { position: absolute; right: 72px; top: 266px; text-align: right; }
  .contact-label { font-family: "Tinos", serif; font-size: 23px; color: var(--ink); }
  .contact-phone .contact-label { color: var(--paper-white); }
  .email-value { font-family: "Roboto Condensed", sans-serif; font-size: 16px; color: var(--paper-white); }
  .phone-value { font-family: "Tinos", serif; font-size: 20px; letter-spacing: 1.5px; color: var(--ink); }

  /* Back */
  .card-back { top: 510px; left: 255px; width: 745px; height: 400px; background: var(--back-blue); display: flex; align-items: center; justify-content: center; }
  .company-echo { position: absolute; left: 0; right: 0; top: 138px; text-align: center; font-family: "Roboto Condensed", sans-serif; font-weight: 700; font-size: 60px; color: rgba(255,255,255,0.12); white-space: nowrap; }
  .company-name { position: relative; font-family: "Roboto Condensed", sans-serif; font-weight: 700; font-size: 44px; color: #ffffff; white-space: nowrap; }
</style>
</head>
<body>
<main class="canvas">
  <section class="card card-front" aria-label="Business card front">
    <div class="band-main"></div>
    <div class="band-name"></div>
    <div class="trim-line left"></div>
    <div class="trim-line right"></div>

    <div class="headline">
      <span class="role-main">Accountant</span>
      <span class="ampersand">&amp;</span>
      <span class="role-sub">Small<br>Business Consultant</span>
    </div>

    <h1 class="person-name"><span class="first">Tomas </span><span class="last">Reyl</span></h1>
    <p class="credential"><span class="light">Registered AS</span><span class="dark">IC Agent 48170</span></p>

    <div class="contact-email">
      <p class="contact-label">Email</p>
      <p class="email-value">tomas@kelvarinledger.com.au</p>
    </div>
    <div class="contact-phone">
      <p class="contact-label">Call</p>
      <p class="phone-value">0400 555 217</p>
    </div>
  </section>

  <section class="card card-back" aria-label="Business card back">
    <p class="company-echo" aria-hidden="true">Kelvarin Ledger Group Pty Ltd</p>
    <p class="company-name">Kelvarin Ledger Group Pty Ltd</p>
  </section>
</main>
</body>
</html>
```